Corvell Executive Search - New Business Card Design Project

We are an executive search firm called Corvell Executive Search based in the UK. We require a custom design for a business card. We're looking to convey a professional service to executives for executive search recruitment services. In terms of colours, we like dark blues and grays (maybe even silver incorporated somewhere if we go for a foiled type of card) but we're open to your artistic flare. See our current logo in attachments. We are totally open on design so long as the design is slick and professional.
Updates

Thanks for all your contributions of various designs. I have to say the quality of work has been amazing which is going to make our job quite difficult in the coming days on making a decision. Thanks to you all that have taken the time to submit designs thus far. We'll keep on reviewing and try to narrow down our selection as soon as possible.

Target Market(s)

Executive Search

Industry/Entity Type

Recruitment

Contact Information for Business Card

Corvell Executive Search,
Exclusively Sourcing & Hiring Senior Leaders
Dominic Haverley, Managing Director,
07742 318906
0117 468 2917
dominic@corvellexecutive.example
corvellexecutive.example
47 Linden Court, Marsh Lane, Bristol, BS9 7QT

Font styles to use
Sans Serif
Other font styles liked:
• Roboto (which is used in our logo)

Requirements
Must have
• Our logo (It has a subtle fade on it from #02071d at top to #333649 at bottom)
• The logo can be on one side or both sides
• Must be elegant and professional
• We have 2nd slogan CONSULT | INSPIRE | INNOVATE | DELIVER which can be incorporated into the card
Nice to have
• Use of blues and grey colours
• Compatible with similar styling to our website corvellexecutive.example
Should not have
• Must not be overly brash
• Must not contain cartoon characters

```html
<!DOCTYPE html>
<html lang="en">
<head>
<meta charset="utf-8">
<title>Corvell Executive Search – Business Card</title>
<link rel="stylesheet" href="https://fonts.googleapis.com/css2?family=Open+Sans:wght@400;600&display=swap">
<style>
  :root {
    --stage: #000000;
    --card-light: #f2f2f2;
    --navy-top: #02071d;
    --navy-bottom: #333649;
    --ink: #1a1f35;
    --ink-soft: #2b2e3c;
    --white: #ffffff;
  }
  * { margin: 0; padding: 0; box-sizing: border-box; }
  html, body { width: 1200px; height: 900px; overflow: hidden; background: var(--stage); }
  .canvas { position: relative; width: 1200px; height: 900px; }

  .card { position: absolute; top: 200px; width: 310px; height: 502px; overflow: hidden; }
  .card-front { left: 265px; background: var(--card-light); border-radius: 62px 0 62px 0; }
  .card-back {
    left: 641px; width: 309px;
    background: linear-gradient(to bottom, #0a0f2a 0%, #1c2035 45%, var(--navy-bottom) 100%);
    border-radius: 0 62px 0 62px;
  }

  .company-name {
    position: absolute; font-family: "Open Sans", sans-serif; font-weight: 600; white-space: nowrap;
  }
  .card-front .brand-square {
    position: absolute; left: 81px; top: 172px; width: 16px; height: 16px; background: var(--navy-top);
  }
  .card-front .company-name {
    left: 107px; top: 163px; font-size: 19px; line-height: 24px; color: var(--ink);
  }

  .holder { position: absolute; left: 22px; font-family: "Open Sans", sans-serif; color: var(--ink); }
  .holder-name { top: 268px; font-size: 17.5px; font-weight: 600; }
  .holder-role { top: 293px; font-size: 13.5px; color: var(--ink-soft); }
  .address { position: absolute; left: 22px; top: 330px; font-family: "Open Sans", sans-serif; font-size: 14px; line-height: 21px; color: var(--ink-soft); }

  .contacts { position: absolute; left: 24px; top: 390px; list-style: none; font-family: "Open Sans", sans-serif; font-size: 13.5px; color: var(--ink-soft); }
  .contacts li { display: flex; align-items: center; height: 21px; }
  .contacts svg { width: 11px; height: 11px; margin-right: 6px; fill: var(--ink); flex: none; }

  .card-back .company-name {
    left: 25px; top: 300px; font-size: 30px; line-height: 38px; color: var(--white);
  }
  .tagline {
    position: absolute; left: 0; width: 309px; top: 403px; text-align: center;
    font-family: "Open Sans", sans-serif; font-weight: 600; font-size: 19px; line-height: 27px; color: var(--white);
  }
</style>
</head>
<body>
<main class="canvas">

  <section class="card card-front" aria-label="Business card front">
    <span class="brand-square" aria-hidden="true"></span>
    <p class="company-name">Corvell<br>Executive Search</p>

    <p class="holder holder-name">Dominic Haverley</p>
    <p class="holder holder-role">Managing Director</p>

    <p class="address">47 Linden Court, Marsh Lane,<br>Bristol, BS9 7QT</p>

    <ul class="contacts">
      <li>
        <svg viewBox="0 0 12 12" aria-hidden="true"><path d="M2.4 0.6l2 2.2-1 1.3c.7 1.5 1.9 2.7 3.4 3.4l1.3-1 2.2 2-1.2 2c-4.5-.3-8.3-4.1-8.6-8.6z"/></svg>
        07742 318906
      </li>
      <li>
        <svg viewBox="0 0 12 12" aria-hidden="true"><path d="M3 0h6a1 1 0 0 1 1 1v10a1 1 0 0 1-1 1H3a1 1 0 0 1-1-1V1a1 1 0 0 1 1-1zm.5 1.5v7.5h5V1.5zM6 9.8a.7.7 0 1 0 0 1.4.7.7 0 0 0 0-1.4z"/></svg>
        0117 468 2917
      </li>
      <li>
        <svg viewBox="0 0 12 12" aria-hidden="true"><path d="M0 2h12v1L6 7 0 3zM0 4.3l6 4 6-4V10H0z"/></svg>
        dominic@corvellexecutive.example
      </li>
      <li>
        <svg viewBox="0 0 12 12" aria-hidden="true"><circle cx="6" cy="6" r="5.5"/></svg>
        corvellexecutive.example
      </li>
    </ul>
  </section>

  <section class="card card-back" aria-label="Business card back">
    <p class="company-name">Corvell<br>Executive Search</p>
    <p class="tagline">Exclusively Sourcing<br>&amp; Hiring Senior Leaders</p>
  </section>

</main>
</body>
</html>
```